Brimvane.com fiber optic internet website redesign

We need a new website design for our fiber optic internet company that provides internet, phone, and tv services. It should use the text "Marrowfen fiber optics", and "I beamed up with Marrowfen". The design should use the color blue and the attached logo.
We are a 30 year old internet company who started as a dial up internet provider in our basement. Today we design, build, and maintain our own fiber optic internet network to provide service to residential, business, educational, healthcare, and governmental customers

```html
<!DOCTYPE html>
<html lang="en">
<head>
<meta charset="utf-8">
<title>Brimvane.com — Marrowfen fiber optics</title>
<link rel="stylesheet" href="https://fonts.googleapis.com/css2?family=Exo+2:wght@400;500;600;700&family=Lato:wght@400;700&display=swap">
<style>
:root{
  --bg:#000;
  --ink:#fff;
  --muted:#cfd6e4;
  --blue:#0b4ea8;
  --blue-bright:#2f6fe0;
  --blue-deep:#062a66;
  --red:#c3203a;
  --card:#141414;
  --card-line:#2c2c34;
  --pale:#cddff4;
  --navy-text:#0b3f8f;
}
*{margin:0;padding:0;box-sizing:border-box}
html,body{width:1200px;height:5068px;overflow:hidden;background:var(--bg)}
body{position:relative;font-family:"Lato",sans-serif;color:var(--ink)}
.abs{position:absolute}
h1,h2,h3,h4,.display{font-family:"Exo 2",sans-serif;font-weight:500}
.accent{color:var(--blue-bright)}
.btn{position:absolute;display:inline-flex;align-items:center;gap:6px;height:26px;padding:0 14px;border-radius:13px;font:700 11px "Lato",sans-serif;color:#fff;background:linear-gradient(90deg,var(--blue) 0%,#3a4aa0 55%,var(--red) 100%);box-shadow:0 0 0 1px rgba(255,255,255,.15)}
.center{left:0;width:1200px;text-align:center}

/* header */
.hero{top:0;left:0;width:1200px;height:720px;background:radial-gradient(ellipse at 50% 20%,#0c3a86 0%,#06204e 40%,#020a1c 75%,#000 100%)}
.logo{display:flex;align-items:center;gap:8px;font:600 16px "Exo 2",sans-serif;color:#fff}
.logo .mark{width:34px;height:34px;border-radius:50%;background:var(--blue);border:2px solid #fff}
.nav{top:28px;left:350px;display:flex;gap:0;font:600 11px "Lato",sans-serif}
.nav a{color:#fff;text-decoration:none;height:26px;line-height:26px;padding:0 13px;margin-right:12px}
.nav a.active{border-radius:13px;background:linear-gradient(90deg,var(--blue),var(--red))}
.tools{top:32px;left:1008px;display:flex;gap:22px}

/* about */
.about-img{left:710px;top:845px;width:420px;height:285px;background:radial-gradient(ellipse at 70% 45%,#7a3cf0 0%,#3b1890 35%,#12083a 65%,#000 100%)}

/* services */
.services-band{top:1255px;left:0;width:1200px;height:495px;background:radial-gradient(ellipse at 50% 40%,#0a3b8a 0%,#05204f 55%,#000 100%)}
.svc-card{width:223px;height:223px;background:var(--blue);border-radius:8px;text-align:center}
.svc-card .ic{margin:26px auto 0;width:56px;height:56px;border-radius:50%;background:#fff;display:flex;align-items:center;justify-content:center}
.svc-card h3{margin-top:20px;font-size:19px;font-weight:500}
.svc-card p{margin:10px auto 0;width:180px;font-size:11px;line-height:19px;color:#dbe6f8}
.arrow{width:32px;height:32px;border-radius:50%;border:1px solid #fff;display:flex;align-items:center;justify-content:center;background:#111}

/* support */
.support-img{left:548px;top:1935px;width:548px;height:360px;background:radial-gradient(ellipse at 30% 55%,#5a2e6e 0%,#22162e 40%,#08080c 75%,#000 100%)}
.support-card{left:93px;top:1995px;width:537px;height:245px;background:var(--card);border:1px solid var(--card-line);border-radius:10px;padding:36px 44px;font-size:12px;line-height:19px;color:#e6e6e6}

/* bundle */
.bundle-img{left:114px;top:2600px;width:452px;height:350px;background:radial-gradient(ellipse at 55% 52%,#d02a56 0%,#5c1f4a 25%,#1c2a4a 60%,#0a1220 100%)}
.perk{left:615px;display:flex;gap:20px}
.perk .tick{width:26px;height:26px;border-radius:50%;background:#fff;display:flex;align-items:center;justify-content:center;flex:none}
.perk h4{font-size:17px;font-weight:600}
.perk p{margin-top:8px;font-size:11.5px;color:var(--muted)}

/* getting started */
.start-band{top:3095px;left:10px;width:1180px;height:545px;background:linear-gradient(180deg,#070d1c 0%,#040812 100%)}
.start-card{top:3262px;width:409px;height:323px;background:var(--card);border:1px solid var(--card-line);border-radius:12px;padding:42px 42px}
.start-card h3{font-size:22px;font-weight:600}
.start-card .sub{margin-top:10px;font-size:12px;color:var(--muted)}
.start-card ul{list-style:none;margin-top:28px}
.start-card li{display:flex;align-items:center;gap:14px;height:50px;font-size:13px}
.start-card li .ic{width:34px;height:34px;border-radius:50%;background:#fff;display:flex;align-items:center;justify-content:center}

/* packages */
.pkg{border-radius:10px;overflow:hidden;background:#fff;color:var(--navy-text);text-align:center}
.pkg .top{background:var(--pale);padding-top:40px}
.pkg h4{font-size:15px;font-weight:600;line-height:19px;color:#14233f}
.pkg ul{list-style:none;display:inline-block;text-align:left;margin-top:18px}
.pkg li{display:flex;align-items:center;gap:8px;font-size:11.5px;height:25px;color:#4a5e80}
.pkg .price{font:700 92px/1 "Exo 2",sans-serif;margin-top:10px}
.pkg .per{font-size:12px;margin-top:6px;padding-bottom:26px}
.pkg.featured .top{background:linear-gradient(180deg,var(--blue) 0%,var(--blue-deep) 100%);color:#fff}
.pkg.featured h4,.pkg.featured li{color:#fff}
.pkg .btn{position:relative;margin-top:28px}

/* cta */
.cta{left:101px;top:4505px;width:1002px;height:158px;background:var(--blue);border-radius:12px}
.cta h2{position:absolute;left:64px;top:42px;font-size:28px;line-height:36px;font-weight:500}
.cta .join{position:absolute;left:811px;top:66px;width:128px;height:28px;border-radius:14px;background:#fff;color:var(--blue);font:700 10px/28px "Lato",sans-serif;text-align:center}

/* footer */
.foot-col h5{font:700 11px "Lato",sans-serif;letter-spacing:.5px;margin-bottom:20px}
.foot-col a{display:block;color:#dfe4ee;text-decoration:none;font-size:10px;height:23.6px}
.social{display:flex;gap:14px}
.social span{width:16px;height:16px;border-radius:50%;background:#fff}
.bottom{top:4998px;left:0;width:1200px;height:70px;background:var(--blue);font-size:9px;color:#e4ebf8}
</style>
</head>
<body>

<!-- Header / hero -->
<section class="abs hero" role="img" aria-label="Glowing blue network of connected points over a dark background"></section>
<div class="abs logo" style="left:100px;top:19px"><span class="mark"></span>Brimvane.com</div>
<nav class="abs nav">
  <a class="active">home</a><a>About Us</a><a>Services</a><a>Support</a><a>Check Availability</a><a>Contact Us</a>
</nav>
<div class="abs tools">
  <svg width="14" height="14" viewBox="0 0 24 24" fill="none" stroke="#fff" stroke-width="2.5"><circle cx="10" cy="10" r="6"/><path d="M15 15l6 6"/></svg>
  <svg width="16" height="16" viewBox="0 0 24 24" fill="none" stroke="#fff" stroke-width="2.2"><path d="M3 11l9-8 9 8v10h-6v-6H9v6H3z"/></svg>
  <svg width="14" height="14" viewBox="0 0 24 24" fill="none" stroke="#fff" stroke-width="2.8"><path d="M3 6h18M3 12h18M3 18h18"/></svg>
</div>
<h1 class="abs center" style="top:196px;font-size:50px;font-weight:500">I Beamed Up with Marrowfen</h1>
<p class="abs center" style="top:302px;font-size:12px;color:var(--muted)">Lightning-fast fiber optic internet, phone, and tv services for homes and businesses</p>
<span class="btn" style="left:550px;top:356px">Get Lit Now</span>

<!-- About -->
<h2 class="abs" style="left:100px;top:864px;font-size:38px;line-height:48px"><span class="accent">30 Years</span> of Connecting You to<br>the World</h2>
<p class="abs" style="left:102px;top:980px;width:540px;font-size:12px;line-height:19px;color:#e0e0e0">From our humble beginnings in a basement providing dial-up internet to designing and maintaining our own fiber optic network today, Marrowfen has been your trusted internet partner</p>
<span class="btn" style="left:99px;top:1073px">Get Lit Now</span>
<div class="abs about-img" role="img" aria-label="Fiber optic network cables glowing in blue and purple"></div>

<!-- Services -->
<section class="abs services-band"></section>
<h2 class="abs center" style="top:1332px;font-size:34px">Services</h2>
<div class="abs arrow" style="left:150px;top:1516px"><svg width="12" height="12" viewBox="0 0 24 24" fill="none" stroke="#fff" stroke-width="3"><path d="M15 4l-8 8 8 8"/></svg></div>
<div class="abs arrow" style="left:1028px;top:1516px"><svg width="12" height="12" viewBox="0 0 24 24" fill="none" stroke="#fff" stroke-width="3"><path d="M9 4l8 8-8 8"/></svg></div>
<div class="abs svc-card" style="left:229px;top:1422px">
  <div class="ic"><svg width="30" height="30" viewBox="0 0 24 24" fill="none" stroke="#0b4ea8" stroke-width="2.4" stroke-linecap="round"><path d="M2 9a15 15 0 0 1 20 0M5 12.5a10 10 0 0 1 14 0M8.5 16a5 5 0 0 1 7 0"/><circle cx="12" cy="19.5" r="1.3" fill="#0b4ea8"/></svg></div>
  <h3>INTERNET</h3><p>Blazing-fast speeds for seamless streaming, gaming, and browsing</p>
</div>
<div class="abs svc-card" style="left:499px;top:1422px">
  <div class="ic"><svg width="30" height="30" viewBox="0 0 24 24" fill="none" stroke="#0b4ea8" stroke-width="2.4" stroke-linecap="round"><path d="M2 9a15 15 0 0 1 20 0M5 12.5a10 10 0 0 1 14 0M8.5 16a5 5 0 0 1 7 0"/><circle cx="12" cy="19.5" r="1.3" fill="#0b4ea8"/></svg></div>
  <h3>INTERNET</h3><p>Blazing-fast speeds for seamless streaming, gaming, and browsing</p>
</div>
<div class="abs svc-card" style="left:769px;top:1422px">
  <div class="ic"><svg width="30" height="30" viewBox="0 0 24 24" fill="none" stroke="#0b4ea8" stroke-width="2.4" stroke-linecap="round"><path d="M2 9a15 15 0 0 1 20 0M5 12.5a10 10 0 0 1 14 0M8.5 16a5 5 0 0 1 7 0"/><circle cx="12" cy="19.5" r="1.3" fill="#0b4ea8"/></svg></div>
  <h3>INTERNET</h3><p>Blazing-fast speeds for seamless streaming, gaming, and browsing</p>
</div>

<!-- Support -->
<h2 class="abs" style="left:93px;top:1846px;font-size:38px">Support from People <span class="accent">Who Care</span></h2>
<p class="abs" style="left:93px;top:1912px;font-size:12px;color:var(--muted)">we're here for you – no outsourcing, just real people ready to help</p>
<div class="abs support-img" role="img" aria-label="Support agent wearing a headset, lit in warm and violet tones"></div>
<div class="abs support-card">
  <p>Marrowfen has been the leading choice for high-quality and superior service since 1995. our reputation is built on having the best customer support in the industry.</p>
  <p style="margin-top:19px">we don't outsource our customer service or technical support – when you call, we answer! experience the difference with local support you can trust</p>
  <span class="btn" style="left:44px;top:172px">Contact Support
    <svg width="12" height="12" viewBox="0 0 24 24" fill="none" stroke="#fff" stroke-width="2.4"><circle cx="12" cy="12" r="9"/><path d="M9.5 9.5a2.5 2.5 0 1 1 3.5 2.3c-.7.4-1 .9-1 1.7M12 17h.01"/></svg></span>
</div>

<!-- Bundle -->
<h2 class="abs center" style="top:2428px;font-size:38px;line-height:48px"><span class="accent">Save Big</span> When You Bundle<br>Internet &amp; Phone</h2>
<p class="abs center" style="top:2538px;font-size:12px;color:var(--muted)">Affordable, reliable service with no hidden fees or surprises</p>
<div class="abs bundle-img" role="img" aria-label="Fiber optic cable glowing pink and red around a dark device"></div>
<div class="abs perk" style="top:2624px"><span class="tick"><svg width="14" height="14" viewBox="0 0 24 24" fill="none" stroke="#000" stroke-width="3.4"><path d="M4 12l5 5L20 6"/></svg></span><div><h4>Unlimited Calling</h4><p>Enjoy unlimited local and long-distance calls within the u.s. and canada</p></div></div>
<div class="abs perk" style="top:2699px"><span class="tick"><svg width="14" height="14" viewBox="0 0 24 24" fill="none" stroke="#000" stroke-width="3.4"><path d="M4 12l5 5L20 6"/></svg></span><div><h4>No Hidden Fees</h4><p>No per-minute charges, installation fees, or surprise rate hikes.</p></div></div>
<div class="abs perk" style="top:2774px"><span class="tick"><svg width="14" height="14" viewBox="0 0 24 24" fill="none" stroke="#000" stroke-width="3.4"><path d="M4 12l5 5L20 6"/></svg></span><div><h4>All-in-One Bill</h4><p>Internet and phone on one easy, low-cost bill.</p></div></div>
<div class="abs perk" style="top:2849px"><span class="tick"><svg width="14" height="14" viewBox="0 0 24 24" fill="none" stroke="#000" stroke-width="3.4"><path d="M4 12l5 5L20 6"/></svg></span><div><h4>Free Features</h4><p>Includes voicemail and caller id at no extra cost.</p></div></div>
<span class="btn" style="left:660px;top:2937px">Big Save</span>

<!-- Getting started -->
<section class="abs start-band"></section>
<h2 class="abs center" style="top:3136px;font-size:38px">Getting <span class="accent">Started</span></h2>
<p class="abs center" style="top:3205px;font-size:12px;color:var(--muted)">Choose the right service for your home or business needs</p>
<div class="abs start-card" style="left:165px">
  <h3>Residential</h3><p class="sub">Fast, Reliable, And Affordable Internet For Your Home.</p>
  <ul>
    <li><span class="ic"><svg width="16" height="16" viewBox="0 0 24 24" fill="none" stroke="#0b4ea8" stroke-width="2.4"><path d="M3 11l9-8 9 8v10h-6v-6H9v6H3z"/></svg></span>Internet Service</li>
    <li><span class="ic"><svg width="16" height="16" viewBox="0 0 24 24" fill="none" stroke="#0b4ea8" stroke-width="2.2"><path d="M5 3h4l2 5-3 2a11 11 0 0 0 6 6l2-3 5 2v4a2 2 0 0 1-2 2A17 17 0 0 1 3 5a2 2 0 0 1 2-2z"/></svg></span>Phone Service</li>
    <li><span class="ic"><svg width="16" height="16" viewBox="0 0 24 24" fill="none" stroke="#0b4ea8" stroke-width="2.2"><circle cx="12" cy="12" r="9"/><path d="M3 12h18M12 3a14 14 0 0 1 0 18M12 3a14 14 0 0 0 0 18"/></svg></span>Internet &amp; Phone Packages</li>
  </ul>
</div>
<div class="abs start-card" style="left:609px">
  <h3>Business</h3><p class="sub">Elevate Your Business With Superior Connectivity.</p>
  <ul>
    <li><span class="ic"><svg width="16" height="16" viewBox="0 0 24 24" fill="none" stroke="#0b4ea8" stroke-width="2.2"><path d="M4 21V5h10v16M14 10h6v11M2 21h20M7 9h4M7 13h4M7 17h4"/></svg></span>Internet Service</li>
    <li><span class="ic"><svg width="16" height="16" viewBox="0 0 24 24" fill="none" stroke="#0b4ea8" stroke-width="2.2"><path d="M5 3h4l2 5-3 2a11 11 0 0 0 6 6l2-3 5 2v4a2 2 0 0 1-2 2A17 17 0 0 1 3 5a2 2 0 0 1 2-2z"/></svg></span>Phone Service</li>
    <li><span class="ic"><svg width="16" height="16" viewBox="0 0 24 24" fill="none" stroke="#0b4ea8" stroke-width="2.2"><circle cx="12" cy="12" r="9"/><path d="M3 12h18M12 3a14 14 0 0 1 0 18M12 3a14 14 0 0 0 0 18"/></svg></span>Internet &amp; Phone Packages</li>
  </ul>
</div>

<!-- Packages -->
<h2 class="abs center" style="top:3770px;font-size:38px">Our <span class="accent">Packages</span></h2>
<p class="abs center" style="top:3832px;font-size:12px;color:var(--muted)">Double the services, double the savings.</p>
<div class="abs pkg" style="left:157px;top:3918px;width:288px;height:487px">
  <div class="top"><h4>High-Speed Internet<br>Service</h4>
    <ul><li><svg width="14" height="14" viewBox="0 0 24 24" fill="none" stroke="currentColor" stroke-width="2.4"><circle cx="12" cy="12" r="9"/><path d="M8 12l3 3 5-6"/></svg>Highest Quality</li><li><svg width="14" height="14" viewBox="0 0 24 24" fill="none" stroke="currentColor" stroke-width="2.4"><circle cx="12" cy="12" r="9"/><path d="M8 12l3 3 5-6"/></svg>Fastest</li><li><svg width="14" height="14" viewBox="0 0 24 24" fill="none" stroke="currentColor" stroke-width="2.4"><circle cx="12" cy="12" r="9"/><path d="M8 12l3 3 5-6"/></svg>Reliable Internet</li><li><svg width="14" height="14" viewBox="0 0 24 24" fill="none" stroke="currentColor" stroke-width="2.4"><circle cx="12" cy="12" r="9"/><path d="M8 12l3 3 5-6"/></svg>R25 Mbps Download</li></ul>
    <div class="price">$55</div><div class="per">Per month</div></div>
  <span class="btn" style="padding:0 34px">Buy Now</span>
</div>
<div class="abs pkg featured" style="left:452px;top:3892px;width:326px;height:540px">
  <div class="top" style="padding-top:48px"><h4>VoIP Phone Service</h4>
    <ul style="margin-top:22px"><li><svg width="14" height="14" viewBox="0 0 24 24" fill="none" stroke="currentColor" stroke-width="2.4"><circle cx="12" cy="12" r="9"/><path d="M8 12l3 3 5-6"/></svg>Free Voicemail</li><li><svg width="14" height="14" viewBox="0 0 24 24" fill="none" stroke="currentColor" stroke-width="2.4"><circle cx="12" cy="12" r="9"/><path d="M8 12l3 3 5-6"/></svg>Caller ID</li><li><svg width="14" height="14" viewBox="0 0 24 24" fill="none" stroke="currentColor" stroke-width="2.4"><circle cx="12" cy="12" r="9"/><path d="M8 12l3 3 5-6"/></svg>UNLIMITED Local</li><li><svg width="14" height="14" viewBox="0 0 24 24" fill="none" stroke="currentColor" stroke-width="2.4"><circle cx="12" cy="12" r="9"/><path d="M8 12l3 3 5-6"/></svg>Long-Distance Calling</li></ul>
    <div class="price" style="margin-top:22px">$25</div><div class="per" style="padding-bottom:30px">Per month</div></div>
  <span class="btn" style="padding:0 34px;margin-top:34px">Buy Now</span>
</div>
<div class="abs pkg" style="left:785px;top:3918px;width:288px;height:487px">
  <div class="top" style="padding-top:34px"><h4>Phone &amp; Internet<br>Packages</h4>
    <ul style="margin-top:14px"><li><svg width="14" height="14" viewBox="0 0 24 24" fill="none" stroke="currentColor" stroke-width="2.4"><circle cx="12" cy="12" r="9"/><path d="M8 12l3 3 5-6"/></svg>Highest Quality</li><li><svg width="14" height="14" viewBox="0 0 24 24" fill="none" stroke="currentColor" stroke-width="2.4"><circle cx="12" cy="12" r="9"/><path d="M8 12l3 3 5-6"/></svg>Fastest</li><li><svg width="14" height="14" viewBox="0 0 24 24" fill="none" stroke="currentColor" stroke-width="2.4"><circle cx="12" cy="12" r="9"/><path d="M8 12l3 3 5-6"/></svg>Reliable Internet</li><li><svg width="14" height="14" viewBox="0 0 24 24" fill="none" stroke="currentColor" stroke-width="2.4"><circle cx="12" cy="12" r="9"/><path d="M8 12l3 3 5-6"/></svg>R25 Mbps Download</li></ul>
    <div class="price">$80</div><div class="per">Per month</div></div>
  <span class="btn" style="padding:0 34px">Buy Now</span>
</div>

<!-- CTA -->
<section class="abs cta">
  <h2>Your Trusted Fiber Optic<br>Provider for Over 30 Years.</h2>
  <span class="join">Join Now</span>
</section>

<!-- Footer -->
<div class="abs logo" style="left:100px;top:4752px"><span class="mark"></span>Brimvane.com</div>
<p class="abs" style="left:101px;top:4830px;width:370px;font-size:12px;line-height:22px;color:#e0e4ec">From our humble beginnings in a basement providing dial-up internet to designing and maintaining our own fiber optic network today, Marrowfen has been your trusted internet partner</p>
<div class="abs foot-col" style="left:561px;top:4738px"><h5>QUICK LINKS</h5><a>Home</a><a>About us</a><a>Services</a><a>Support</a><a>Benefits</a><a>Getting Started</a><a>Our Services</a></div>
<div class="abs foot-col" style="left:762px;top:4738px"><h5>SERVICES</h5><a>Internet</a><a>Phone</a><a>Tv</a></div>
<div class="abs foot-col" style="left:979px;top:4738px"><h5>STAY &nbsp;CONNECTED</h5><div class="social"><span></span><span></span><span></span></div></div>
<div class="abs bottom">
  <span class="abs" style="left:98px;top:30px">Copyright © 2024, <b>Website</b>. All rights reserved.</span>
  <span class="abs" style="left:968px;top:30px">Privacy Policy &nbsp;|&nbsp; Terms of Use</span>
</div>

</body>
</html>
```